Website redesign

We've inherited a Tilecraft Website that we'd like to change to a Pagemill website to match our other sites.

Site I want redesigned is: https://www.corvellawings.com/
which will change to www.corvellaskytours.com.au

Our other websites I want it to match:
https://marloweskytours.com.au/
https://penfaricays.au/
https://tindaleskytours.com.au/
https://brightvalewings.com.au/

I do not want the design to deviate too much from the others, the main difference will be colours that need to align with the logo I've uploaded.

Pages I want:
Home
About Us
Gallery
News/Blog
Overflies
Half Day Tours
Full Day Tours
Transfers
Contact

Other pages will link to the other website - like on the other websites currently

```html
<!DOCTYPE html>
<html lang="en">
<head>
<meta charset="utf-8">
<title>Corvella Sky Tours – Scenic Flights</title>
<link href="https://fonts.googleapis.com/css2?family=Arimo:wght@400;500;600;700&display=swap" rel="stylesheet">
<style>
:root{
  --ink:#222;
  --topbar:#141414;
  --sky:#4a9fd8;
  --sky-band:#5d9fcf;
  --green:#7fb740;
  --green-soft:#eef5e4;
  --footer:#0b76d4;
  --white:#fff;
  --muted:#555;
}
*{box-sizing:border-box;margin:0;padding:0}
html,body{width:1200px;height:3930px;overflow:hidden}
body{font-family:"Arimo",Arial,sans-serif;color:var(--ink);background:var(--white);position:relative}
.abs{position:absolute}
a{color:inherit;text-decoration:none}

.topbar{left:0;top:0;width:1200px;height:55px;background:var(--topbar);color:#eee;font-size:15px}
.topbar .contact{left:111px;top:19px;display:flex;gap:30px}
.topbar .contact span{display:flex;align-items:center;gap:8px}
.topbar .social{right:111px;top:17px;display:flex;align-items:center;gap:12px}
.dot{width:18px;height:18px;border-radius:4px;background:var(--green)}
.dot.round{border-radius:50%}

.header{left:0;top:55px;width:1200px;height:97px;background:var(--white)}
.brand{left:111px;top:30px;display:flex;align-items:center;gap:10px;font-size:26px;font-weight:600;color:var(--sky)}
.brand i{width:34px;height:34px;border-radius:50%;background:var(--sky);display:block}
.nav{left:500px;top:39px;display:flex;gap:31px;font-size:15px;color:#333}
.nav .active{color:var(--sky);font-weight:600}

.hero{left:0;top:152px;width:1200px;height:456px;background:linear-gradient(100deg,#3f8c93 0%,#79a9a6 30%,#cfcbc0 55%,#d9d2c4 70%,#c0a25a 85%,#b89a4e 100%)}
.hero h1{left:111px;top:69px;width:420px;font-size:44px;line-height:50px;font-weight:600;color:var(--white)}
.hero p{left:111px;top:244px;width:500px;font-size:16px;line-height:26px;color:var(--white)}
.btn{display:flex;align-items:center;justify-content:center;height:40px;font-size:17px;border-radius:4px}
.btn.solid{background:var(--green);color:var(--white)}
.btn.ghost{border:2px solid var(--white);color:var(--white)}
.btn.light{background:var(--white);color:var(--sky)}
.hero .b1{left:111px;top:342px;width:168px}
.hero .b2{left:308px;top:342px;width:169px}

.about-img1{left:111px;top:694px;width:299px;height:348px;border-radius:8px 0 0 8px;background:linear-gradient(180deg,#f0b489 0%,#b6a4a0 20%,#8a6a5a 45%,#3eb2b8 75%,#2aa6b8 100%)}
.about-img2{left:338px;top:815px;width:231px;height:303px;border:10px solid var(--white);border-radius:14px;background:linear-gradient(180deg,#cfd8e0 0%,#9fb1c4 40%,#c94a3a 70%,#7d8fa3 100%)}
.faint-name{left:432px;top:740px;font-size:34px;font-weight:600;color:#d4e6f4}
.about h2{left:630px;top:713px;width:480px;font-size:36px;line-height:46px;font-weight:500;color:var(--sky)}
.about p{left:630px;top:834px;width:460px;font-size:14.5px;line-height:26px;color:#333}
.feature{top:938px;display:flex;align-items:center;gap:14px;font-size:18px;line-height:23px}
.feature svg{width:64px;height:50px}
.about .rule{left:630px;top:1011px;width:452px;height:1px;background:#ddd}
.about .b3{left:630px;top:1035px;width:168px;height:39px}

.stat{top:1154px;width:230px;text-align:center}
.stat .circle{margin:0 auto;width:110px;height:110px;border-radius:50%;background:var(--green-soft);display:flex;align-items:center;justify-content:center}
.stat b{display:block;margin-top:14px;font-size:25px;font-weight:500;color:var(--sky)}
.stat span{display:block;font-size:15px;color:#333;margin-top:3px}
.vline{top:1202px;width:3px;height:76px;background:var(--green)}

.band{left:0;top:1410px;width:1200px;height:524px;background:linear-gradient(180deg,#5a9dcf,#6aa6d3 60%,#5e9ccc)}
.band h2{left:114px;top:78px;width:520px;font-size:35px;line-height:46px;font-weight:500;color:var(--white)}
.band p{left:114px;top:248px;width:500px;font-size:15px;line-height:26px;color:var(--white)}
.band .b4{left:114px;top:398px;width:168px}
.band .b5{left:311px;top:398px;width:169px}
.video{left:683px;top:100px;width:406px;height:324px;border-radius:6px;background:linear-gradient(100deg,#2fa9a3 0%,#a9ddd7 40%,#efe3cf 52%,#e2c193 70%,#d9b482 100%)}
.video .play{left:173px;top:132px;width:60px;height:60px;border-radius:50%;background:var(--green);display:flex;align-items:center;justify-content:center}

.section-title{left:0;width:1200px;text-align:center;font-size:36px;font-weight:500;color:var(--sky)}
.card{top:2089px;width:215px}
.card .photo{height:272px;border-radius:14px}
.card p{margin-top:30px;font-size:16px;line-height:24px;color:#222}

.review-bg{left:0;top:2539px;width:1200px;height:488px;background:linear-gradient(110deg,#2f6b4a 0%,#1fa7a7 25%,#20a2b8 55%,#1b95b4 80%,#2a8a9a 100%)}
.review{left:111px;top:2672px;width:540px;height:419px;background:var(--white);box-shadow:0 4px 14px rgba(0,0,0,.12);text-align:center}
.review h2{margin-top:40px;font-size:35px;line-height:47px;font-weight:500;color:var(--sky)}
.review .badge{margin:22px auto 0;width:74px;height:54px;border-radius:50%;background:var(--green)}
.review p{margin:26px auto 0;width:440px;font-size:14.5px;line-height:25.5px;color:#333}
.review .name{margin-top:12px;font-size:21px}

.follow{width:216px;border-radius:14px}

.footer{left:0;top:3709px;width:1200px;height:221px;background:var(--footer);color:var(--white)}
.footer .brand-f{left:0;width:1200px;top:53px;display:flex;justify-content:center;align-items:center;gap:10px;font-size:27px;font-weight:600}
.footer .brand-f i{width:34px;height:34px;border-radius:50%;background:var(--white);display:block}
.footer .links{left:0;width:1200px;top:119px;display:flex;justify-content:center;gap:52px;font-size:15px;font-weight:500}
.footer .rule{left:111px;top:160px;width:978px;height:1px;background:rgba(255,255,255,.55)}
.footer .copy{left:111px;top:179px;font-size:12.5px}
.footer .social{right:111px;top:180px;display:flex;gap:14px}
.footer .social .dot{background:var(--white)}
</style>
</head>
<body>

<div class="abs topbar">
  <div class="abs contact">
    <span><svg width="14" height="14" viewBox="0 0 24 24" fill="#7fb740"><path d="M6.6 10.8a15 15 0 0 0 6.6 6.6l2.2-2.2c.3-.3.7-.4 1-.2 1.1.4 2.3.6 3.6.6.6 0 1 .4 1 1V20c0 .6-.4 1-1 1A17 17 0 0 1 3 4c0-.6.4-1 1-1h3.5c.6 0 1 .4 1 1 0 1.3.2 2.5.6 3.6.1.3 0 .7-.2 1z"/></svg>08 9471 2285</span>
    <span><svg width="15" height="12" viewBox="0 0 24 18" fill="#7fb740"><path d="M0 0h24v18H0z"/><path d="M0 0l12 9 12-9" stroke="#141414" stroke-width="2" fill="none"/></svg>info@brightvalewings.com.au</span>
  </div>
  <div class="abs social"><span>Connect With Us</span><i class="dot round"></i><i class="dot"></i><i class="dot round"></i></div>
</div>

<header class="abs header">
  <div class="abs brand"><i></i>Corvella Sky Tours</div>
  <nav class="abs nav">
    <a class="active">Home</a><a>About Us</a><a>Gallery</a><a>News</a><a>Overflies</a><a>Transfers</a>
    <a>More <svg width="10" height="7" viewBox="0 0 10 7"><path d="M1 1l4 4 4-4" stroke="#333" stroke-width="1.6" fill="none"/></svg></a>
  </nav>
</header>

<section class="abs hero" role="img" aria-label="Aerial view of a white sand beach meeting turquoise water and golden cliffs">
  <h1 class="abs">Scenic Flights - Day Tours - Charter - Airwork</h1>
  <p class="abs">Lorem ipsum dolor sit amet, consectetur adipiscing elit, sed do eiusmod tempor incididunt ut labore et dolore magna aliqua. Quis ipsum suspendisse ultrices gravida. Risus commodo</p>
  <a class="abs btn solid b1">Contact Us</a>
  <a class="abs btn ghost b2">Book Now</a>
</section>

<section class="about">
  <div class="abs about-img1" role="img" aria-label="Sunset over a red coastline and turquoise bay seen from the air"></div>
  <div class="abs faint-name">Corvella</div>
  <div class="abs about-img2" role="img" aria-label="Passenger photographing the coast through an aircraft window"></div>
  <h2 class="abs">Your Gateway To Corvella Bay Aerial Wonders</h2>
  <p class="abs">Lorem ipsum dolor sit amet, consectetur adipiscing elit, sed do eiusmod tempor incididunt ut labore et dolore magna aliqua. Quis ipsum suspendisse ultrices gravida. Risus commodo viverra</p>
  <div class="abs feature" style="left:630px">
    <svg viewBox="0 0 64 50" fill="none" stroke="#7fb740" stroke-width="2.4"><path d="M4 36l10-2 14-10 18-14c4-3 10-1 8 3L42 26 34 44l-5 1 2-14-12 8-4 8-4 1 1-9z"/></svg>
    <span>35 Years<br>Experience</span>
  </div>
  <div class="abs feature" style="left:875px">
    <svg viewBox="0 0 64 50" fill="none" stroke="#7fb740" stroke-width="2.4"><rect x="10" y="8" width="40" height="38" rx="6"/><path d="M20 8V3h20v5M18 18h24M18 28h24M18 38h24"/></svg>
    <span>Wide range<br>of Tours</span>
  </div>
  <div class="abs rule"></div>
  <a class="abs btn solid b3">Discover More</a>
</section>

<section class="stats">
  <div class="abs stat" style="left:129px"><div class="circle"><svg width="52" height="52" viewBox="0 0 24 24" fill="#7fb740"><path d="M21 3c-1-1-3 0-4 1l-3 3-8-2-2 2 6 4-3 3-3-.5-1.5 1.5 3.5 2 2 3.5L9.5 19 9 16l3-3 4 6 2-2-2-8 3-3c1-1 2-3 1-4z"/></svg></div><b>15+</b><span>Scenic Fights &amp; Charters</span></div>
  <div class="abs vline" style="left:389px"></div>
  <div class="abs stat" style="left:390px"><div class="circle"><svg width="54" height="50" viewBox="0 0 24 22" fill="#7fb740"><path d="M1 4l7-3 8 3 7-3v17l-7 3-8-3-7 3z"/><path d="M8 1v17M16 4v17" stroke="#eef5e4" stroke-width="1.2"/></svg></div><b>5+</b><span>Destinations</span></div>
  <div class="abs vline" style="left:621px"></div>
  <div class="abs stat" style="left:623px"><div class="circle"><svg width="54" height="54" viewBox="0 0 24 24" fill="none" stroke="#7fb740" stroke-width="1.8"><path d="M7 2a4 4 0 0 1 4 4c0 3-4 7-4 7S3 9 3 6a4 4 0 0 1 4-4z"/><path d="M7 15v2h8a2 2 0 0 1 0 4H5"/><path d="M17 13V4l5 3-5 3" fill="#7fb740"/></svg></div><b>550+</b><span>Scenic Trips</span></div>
  <div class="abs vline" style="left:854px"></div>
  <div class="abs stat" style="left:861px"><div class="circle"><svg width="56" height="50" viewBox="0 0 28 24" fill="#7fb740"><circle cx="14" cy="10" r="3"/><circle cx="7" cy="12" r="2.5"/><circle cx="21" cy="12" r="2.5"/><path d="M8 22a6 6 0 0 1 12 0zM2 22a5 5 0 0 1 7-4v4zM26 22a5 5 0 0 0-7-4v4z"/><path d="M14 1l1 2 2 .3-1.5 1.4.4 2.1L14 5.8l-1.9 1 .4-2.1L11 3.3l2-.3zM6 3l.8 1.6 1.7.2-1.2 1.2.3 1.7L6 6.9l-1.6.8.3-1.7-1.2-1.2 1.7-.2zM22 3l.8 1.6 1.7.2-1.2 1.2.3 1.7-1.6-.8-1.6.8.3-1.7-1.2-1.2 1.7-.2z"/></svg></div><b>3,600+</b><span>Happy Customers</span></div>
</section>

<section class="abs band">
  <h2 class="abs">Fly With Us To Discover The Gem Of The Coral Coast, The Corvella Bay Islands</h2>
  <p class="abs">Lorem ipsum dolor sit amet, consectetur adipiscing elit, sed do eiusmod tempor incididunt ut labore et dolore magna aliqua. Ut enim ad minim veniam, quis nostrud exercitation ullamco laboris nisi ut aliquip ex ea commodo consequat. Duis aute irure dolor in reprehenderit in voluptate velit</p>
  <a class="abs btn light b4">Contact Us</a>
  <a class="abs btn ghost b5">Book Now</a>
  <div class="abs video" role="img" aria-label="Video still of waves breaking on a sandy beach with an aircraft shadow">
    <div class="abs play"><svg width="22" height="24" viewBox="0 0 22 24"><path d="M2 1l19 11L2 23z" fill="#fff"/></svg></div>
  </div>
</section>

<section class="excursions">
  <h2 class="abs section-title" style="top:2008px">Explore Our Excursions</h2>
  <div class="abs card" style="left:111px"><div class="photo" role="img" aria-label="Aerial view of red dunes beside a green sea" style="background:linear-gradient(110deg,#5e9a82 0%,#b9c7a8 45%,#c8562a 60%,#b5461f 100%)"></div><p>Lorem ipsum dolor sit amet, consectetur adipiscing elit, sed do eiusmod tempor</p></div>
  <div class="abs card" style="left:364px"><div class="photo" role="img" aria-label="Light aircraft parked on a red dirt airstrip" style="background:linear-gradient(180deg,#d5d5d8 0%,#b9b8b8 45%,#9d7a5a 70%,#5a3d2b 100%)"></div><p>Lorem ipsum dolor sit amet, consectetur adipiscing elit, sed do eiusmod tempor</p></div>
  <div class="abs card" style="left:618px"><div class="photo" role="img" aria-label="Pilot beside the wing of an aircraft under a blue sky" style="background:linear-gradient(180deg,#2e5fb0 0%,#5b8fd0 45%,#e8e8ea 55%,#5f7d4a 100%)"></div><p>Lorem ipsum dolor sit amet, consectetur adipiscing elit, sed do eiusmod tempor</p></div>
  <div class="abs card" style="left:871px"><div class="photo" role="img" aria-label="Passenger photographing the bay from inside a light aircraft" style="background:linear-gradient(110deg,#b7b3ae 0%,#8fc0c0 35%,#50a4a8 55%,#3f3f42 80%,#2e2e30 100%)"></div><p>Lorem ipsum dolor sit amet, consectetur adipiscing elit, sed do eiusmod tempor</p></div>
</section>

<div class="abs review-bg" role="img" aria-label="Aerial view of green islands scattered in turquoise water"></div>
<section class="abs review">
  <h2>What Customer Say<br>About Us</h2>
  <div class="badge"></div>
  <p>“Lorem ipsum dolor sit amet, consectetur adipiscing elit, sed do eiusmod tempor incididunt ut labore et dolore magna aliqua. Ut enim ad minim veniam, quis nostrud exercitation ullamco laboris nisi ”</p>
  <div class="name">-Daniel Hart</div>
</section>

<section class="gallery">
  <h2 class="abs section-title" style="top:3167px">Follow #corvellabay</h2>
  <div class="abs follow" style="left:111px;top:3260px;height:301px;background:linear-gradient(180deg,#6a7c92 0%,#e9a453 35%,#c77a3c 55%,#4a4347 100%)" role="img" aria-label="Aircraft on an airstrip at sunset"></div>
  <div class="abs follow" style="left:364px;top:3320px;height:299px;background:linear-gradient(160deg,#c46c4c 0%,#d99a7a 35%,#8a6a54 60%,#5f6d72 100%)" role="img" aria-label="Aerial view of red cliffs and shallow bay"></div>
  <div class="abs follow" style="left:619px;top:3260px;height:301px;background:linear-gradient(180deg,#7fa87a 0%,#8cb06f 50%,#9ab874 100%)" role="img" aria-label="Aircraft wing over green farmland"></div>
  <div class="abs follow" style="left:872px;top:3320px;height:299px;background:linear-gradient(180deg,#3f8fcf 0%,#7fb5cc 35%,#9aa79a 60%,#5b8c8a 100%)" role="img" aria-label="Aerial view of coastline and tidal flats"></div>
</section>

<footer class="abs footer">
  <div class="abs brand-f"><i></i>Corvella Sky Tours</div>
  <nav class="abs links"><a>Home</a><a>About Us</a><a>Gallery</a><a>News</a><a>Overflies</a><a>Transfers</a><a>Contact</a></nav>
  <div class="abs rule"></div>
  <div class="abs copy">Copyright © 2025 Corvella Sky Tours. All rights reserved.</div>
  <div class="abs social"><i class="dot round"></i><i class="dot"></i><i class="dot round"></i></div>
</footer>

</body>
</html>
```